VerdaMetrix PowerPoint Presentation Design

I am looking for a PowerPoint design for a new company based in Dallas, Texas called VerdaMetrix. We provide extremely powerful predictive and prescriptive analytics software focused on the Internet of Things (IoT) market. Our initial products are called VMX Foundry and VMX Pulse. We would like to see designs that support our logo design, which is attached.

I AM LOOKING FOR A THEME TO BE DEVELOPED FOR THE TITLE SLIDE AND INSIDE SLIDES OF A PRESENTATION. I AM NOT LOOKING FOR SOMEONE TO TAKE MY CONTENT AND CREATE A COMPLETE PRESENTATION.

Target Market(s)

Advanced Analytics, Internet of Things

Industry/Entity Type

It Company

Requirements
Must have
• Bolder colors, but they must work with the logo
Nice to have
• I prefer that the design incorporate the them of "connectivity" or "connectedness" to reflect the IoT market and "intelligence" or "smart" to reflect the analytics aspect of the business
Should not have
• I don't want people represented in the graphics scheme

```html
<!DOCTYPE html>
<html lang="en">
<head>
<meta charset="utf-8">
<title>Organisation chart concepts</title>
<link href="https://fonts.googleapis.com/css2?family=Arimo:wght@400;700&display=swap" rel="stylesheet">
<style>
  :root {
    --ink: #000000;
    --muted: #333333;
    --brand-blue: #0a3cff;
    --soft-blue: #829dff;
    --orange: #f59e00;
    --dark: #3f3f3f;
    --grey: #d9d9d9;
    --rule: #b8b8c8;
    --connector: #bdbdbd;
    --paper: #ffffff;
  }
  html, body {
    margin: 0;
    padding: 0;
    width: 1200px;
    height: 831px;
    overflow: hidden;
    background: var(--paper);
  }
  .slide {
    position: relative;
    width: 1200px;
    height: 831px;
    font-family: "Arimo", Arial, sans-serif;
    color: var(--ink);
    overflow: hidden;
  }
  .slide-title {
    position: absolute;
    left: 23px;
    top: 12px;
    margin: 0;
    font-size: 34px;
    font-weight: 700;
  }
  .slide-subtitle {
    position: absolute;
    left: 23px;
    top: 58px;
    margin: 0;
    font-size: 26px;
    font-weight: 400;
    color: var(--muted);
  }
  .brand {
    position: absolute;
    right: 28px;
    top: 30px;
    display: flex;
    align-items: center;
    gap: 6px;
    font-size: 25px;
    font-weight: 700;
    color: var(--brand-blue);
  }
  .brand-dot {
    width: 9px;
    height: 9px;
    border-radius: 50%;
    background: var(--orange);
  }
  .header-rule {
    position: absolute;
    left: 0;
    top: 107px;
    width: 1000px;
    height: 3px;
    background: linear-gradient(90deg, var(--brand-blue), rgba(10, 60, 255, 0.25) 60%, rgba(10, 60, 255, 0));
  }
  .section-heading {
    position: absolute;
    left: 23px;
    top: 133px;
    margin: 0;
    font-size: 18px;
    font-weight: 700;
  }
  .section-rule {
    position: absolute;
    left: 23px;
    top: 157px;
    width: 1151px;
    height: 1px;
    background: var(--rule);
  }
  .section-band {
    position: absolute;
    left: 23px;
    top: 468px;
    width: 1151px;
    height: 37px;
    background: var(--orange);
    box-shadow: 0 3px 4px rgba(0, 0, 0, 0.3);
    display: flex;
    align-items: center;
    padding-left: 12px;
    box-sizing: border-box;
    font-size: 18px;
    font-weight: 700;
  }
  .connectors {
    position: absolute;
    left: 0;
    top: 0;
  }
  .node {
    position: absolute;
    width: 222px;
    display: flex;
    flex-direction: column;
    align-items: center;
    justify-content: center;
    text-align: center;
  }
  .node-label {
    font-size: 14px;
    font-weight: 700;
    line-height: 1.2;
  }
  .node-note {
    font-size: 9px;
    line-height: 1.3;
  }
  .square .node { height: 51px; }
  .rounded .node { height: 48px; border-radius: 6px; }
  .node.lead { background: var(--brand-blue); color: #ffffff; }
  .node.unit { background: var(--soft-blue); }
  .node.team { background: var(--orange); }
  .node.dark { background: var(--dark); color: #ffffff; }
  .node.sub { background: var(--grey); }
  .page-number {
    position: absolute;
    left: 594px;
    top: 797px;
    font-size: 13px;
  }
  .classification {
    position: absolute;
    right: 26px;
    top: 797px;
    font-size: 13px;
  }
</style>
</head>
<body>
<main class="slide">
  <h1 class="slide-title">Slide title</h1>
  <p class="slide-subtitle">subtitle</p>
  <div class="brand"><span>VerdaMetrix</span><span class="brand-dot"></span></div>
  <div class="header-rule"></div>

  <h2 class="section-heading">Organisation chart concept 1</h2>
  <div class="section-rule"></div>

  <svg class="connectors" width="1200" height="831" viewBox="0 0 1200 831" aria-hidden="true">
    <g stroke="var(--connector)" stroke-width="1.5" fill="none">
      <path d="M600 217V229M134 229H1063M134 229V242M445 229V242M754 229V242M1063 229V242"/>
      <path d="M134 292V318M445 292V318M754 292V318M1063 292V318M445 369V395M754 369V395"/>
      <path d="M600 560V572M134 572H1063M134 572V585M445 572V585M754 572V585M1063 572V585"/>
      <path d="M134 632V658M445 632V658M754 632V658M1063 632V658M445 706V731M754 706V731"/>
    </g>
  </svg>

  <section class="org-chart square">
    <div class="node lead" style="left:489px;top:165px"><span class="node-label">Level 1</span><span class="node-note">xxx</span></div>
    <div class="node unit" style="left:23px;top:242px"><span class="node-label">Level 2</span><span class="node-note">xxx</span></div>
    <div class="node unit" style="left:334px;top:242px"><span class="node-label">Level 2</span><span class="node-note">xxx</span></div>
    <div class="node unit" style="left:643px;top:242px"><span class="node-label">Level 2</span><span class="node-note">xxx</span></div>
    <div class="node unit" style="left:952px;top:242px"><span class="node-label">Level 2</span><span class="node-note">xxx</span></div>
    <div class="node team" style="left:23px;top:318px"><span class="node-label">Level 2</span><span class="node-note">xxx</span></div>
    <div class="node team" style="left:334px;top:318px"><span class="node-label">Level 2</span><span class="node-note">xxx</span></div>
    <div class="node team" style="left:643px;top:318px"><span class="node-label">Level 2</span><span class="node-note">xxx</span></div>
    <div class="node team" style="left:952px;top:318px"><span class="node-label">Level 2</span><span class="node-note">xxx</span></div>
    <div class="node sub" style="left:334px;top:395px"><span class="node-label">Level 2</span><span class="node-note">xxx</span></div>
    <div class="node sub" style="left:643px;top:395px"><span class="node-label">Level 2</span><span class="node-note">xxx</span></div>
  </section>

  <div class="section-band">Organisation chart concept 2</div>

  <section class="org-chart rounded">
    <div class="node lead" style="left:489px;top:512px"><span class="node-label">Level 1</span><span class="node-note">xxx</span></div>
    <div class="node unit" style="left:23px;top:585px"><span class="node-label">Level 2</span><span class="node-note">xxx</span></div>
    <div class="node unit" style="left:334px;top:585px"><span class="node-label">Level 2</span><span class="node-note">xxx</span></div>
    <div class="node unit" style="left:643px;top:585px"><span class="node-label">Level 2</span><span class="node-note">xxx</span></div>
    <div class="node unit" style="left:952px;top:585px"><span class="node-label">Level 2</span><span class="node-note">xxx</span></div>
    <div class="node dark" style="left:23px;top:658px"><span class="node-label">Level 2</span><span class="node-note">xxx</span></div>
    <div class="node dark" style="left:334px;top:658px"><span class="node-label">Level 2</span><span class="node-note">xxx</span></div>
    <div class="node dark" style="left:643px;top:658px"><span class="node-label">Level 2</span><span class="node-note">xxx</span></div>
    <div class="node dark" style="left:952px;top:658px"><span class="node-label">Level 2</span><span class="node-note">xxx</span></div>
    <div class="node sub" style="left:334px;top:731px"><span class="node-label">Level 2</span><span class="node-note">xxx</span></div>
    <div class="node sub" style="left:643px;top:731px"><span class="node-label">Level 2</span><span class="node-note">xxx</span></div>
  </section>

  <div class="page-number">5</div>
  <div class="classification">INTERNAL</div>
</main>
</body>
</html>
```